Jazz: Journey Through the Harlem Renaissance and the Black Arts Movement

Corvel Tavern invites you on a musical Journey Through the Harlem Renaissance and the Black Arts Movement!
Join us for an afternoon of Jazz on Sunday, February 27, 2022 from 3pm – 5pm.
Local jazz artists will thrill you with the music of legendary Harlem Renaissance artists such as Royce Tamberlin and Odessa Crane and famed Black Arts Movement stylings reminiscent of Vernon Askew and Lydia Farrow.
There will be games, prizes and opportunities to support arts programs at local schools.

```html
<!DOCTYPE html>
<html lang="en">
<head>
<meta charset="utf-8">
<title>Corvel Tavern – An Afternoon of Jazz</title>
<link rel="stylesheet" href="https://fonts.googleapis.com/css2?family=Playfair+Display:ital,wght@0,400;0,700;1,400;1,700;1,900&family=Merriweather:wght@400&family=Pacifico&display=swap">
<style>
  :root {
    --gold: #d9a920;
    --gold-light: #f6d25a;
    --gold-deep: #a97a0c;
    --ink: #060404;
    --white: #ffffff;
    --ember: #6b2a07;
    --violet: #2a1450;
  }
  * { margin: 0; padding: 0; box-sizing: border-box; }
  html, body { width: 990px; height: 1200px; overflow: hidden; background: #8a8a8a; }
  .poster {
    position: relative;
    width: 990px; height: 1200px;
    background: linear-gradient(135deg, var(--gold-light), var(--gold) 45%, var(--gold-deep) 80%, var(--gold-light));
  }
  .stage {
    position: absolute; inset: 23px;
    overflow: hidden;
    background:
      radial-gradient(ellipse 260px 160px at 210px 30px, rgba(42,20,80,.75), transparent 70%),
      radial-gradient(ellipse 420px 300px at 330px 1140px, rgba(120,52,10,.9), transparent 70%),
      radial-gradient(ellipse 380px 420px at 210px 520px, rgba(70,40,10,.55), transparent 70%),
      var(--ink);
  }
  .hairline {
    position: absolute; inset: 11px;
    border: 1px solid var(--gold);
  }
  .saxophone-art {
    position: absolute; left: 14px; top: 92px; width: 493px; height: 940px;
    background: radial-gradient(ellipse at 45% 55%, #e9b73a 0%, #b9820f 35%, rgba(90,50,5,.4) 65%, transparent 80%);
  }
  .headline, .text { position: absolute; font-family: "Playfair Display", serif; }
  .title {
    left: 245px; top: 52px; width: 700px; text-align: center;
    font-size: 80px; font-style: italic; font-weight: 700;
    color: var(--gold); letter-spacing: .5px; line-height: 1;
  }
  .invite {
    left: 345px; top: 138px; width: 480px; text-align: center;
    font-family: "Pacifico", cursive; font-size: 50px; color: var(--white); line-height: 1.2;
  }
  .journey-pill {
    position: absolute; left: 302px; top: 218px; width: 557px; height: 46px;
    border: 2px solid var(--gold); border-radius: 23px;
    font-family: "Playfair Display", serif; font-size: 29px; color: var(--white);
    text-align: center; line-height: 41px;
  }
  .movement {
    left: 280px; top: 283px; width: 600px; text-align: center;
    font-size: 42px; font-style: italic; color: var(--white); line-height: 54px;
  }
  .movement strong { font-weight: 700; }
  .join {
    right: 75px; top: 408px;
    font-family: "Pacifico", cursive; font-size: 42px; color: var(--gold); line-height: 1.2;
  }
  .afternoon {
    right: 75px; top: 468px;
    font-family: "Merriweather", serif; font-size: 29px; color: var(--white); line-height: 1.2;
  }
  .date-pill {
    position: absolute; left: 388px; top: 510px; width: 500px; height: 48px;
    border-radius: 24px;
    background: linear-gradient(90deg, var(--gold-deep), var(--gold-light) 50%, var(--gold-deep));
    font-family: "Playfair Display", serif; font-size: 33px; font-style: italic; font-weight: 900;
    color: #1a1005; text-align: center; line-height: 48px;
  }
  .hours {
    left: 560px; top: 570px; width: 300px; text-align: center;
    font-family: "Merriweather", serif; font-size: 30px; color: var(--gold); line-height: 1.3;
  }
  .lineup {
    right: 75px; top: 650px; width: 420px; text-align: right;
    font-family: "Merriweather", serif; font-size: 17.5px; color: var(--white); line-height: 25.5px;
  }
  .venue-mark {
    position: absolute; left: 615px; top: 880px; width: 260px;
    display: flex; flex-direction: column; align-items: center; gap: 16px;
  }
  .venue-mark .dot {
    width: 64px; height: 64px; border-radius: 50%; border: 2px solid var(--gold);
  }
  .venue-mark .name {
    font-family: "Playfair Display", serif; font-size: 34px; font-weight: 400; color: var(--gold);
    letter-spacing: 2px;
  }
  .perks {
    left: 57px; top: 1040px; width: 560px;
    font-size: 24px; font-style: italic; font-weight: 700; color: var(--white); line-height: 32px;
  }
</style>
</head>
<body>
<main class="poster">
  <section class="stage">
    <div class="hairline"></div>
    <div class="saxophone-art" role="img" aria-label="Glowing golden saxophone illustration"></div>

    <h1 class="headline title">Corvel Tavern</h1>
    <p class="headline invite">invites you</p>
    <p class="journey-pill">on a musical journey through the</p>
    <h2 class="headline movement"><strong>Harlem Renaissance</strong><br>and the <strong>Black Arts Movement!</strong></h2>

    <p class="text join">Join us for</p>
    <p class="text afternoon">an afternoon of Jazz on</p>
    <p class="date-pill">Sunday, February 27, 2022</p>
    <p class="text hours">from 3pm – 5pm</p>

    <p class="text lineup">Local jazz artists will thrill you<br>with the music of legendary<br>Harlem Renaissance artists such<br>as Royce Tamberlin and Odessa Crane<br>and famed Black Arts Movement<br>stylings reminiscent of<br>Vernon Askew and Lydia Farrow.</p>

    <div class="venue-mark">
      <span class="dot"></span>
      <span class="name">Corvel Tavern</span>
    </div>

    <p class="text perks">There will be games, prizes and opportunities<br>to support arts programs at local schools.</p>
  </section>
</main>
</body>
</html>
```